Business Card Design

I am a florist specialising in weddings. I would like a very modern however elegant and simple design. My arrangement designs can be quite rustic with a vintage feel, so if you are able to reflect this in the card that would be great.
Updates

Thank you everyone for your submissions. I have found some further words for inspiration. I am looking for something more earthy and artisan looking. If possible I would like to use 100% recycled paper - the type that even looks rustic and recycled. I may even opt to use a small logo to emphasis the fact that they are made from recycled paper. I know this is quite different to my original brief but I wasn't quite sure what to expect from your designs. Also, with the logo, I give permission for it to be cropped to remove the 'Floral Designer' text. Please contact me if you need any further assistance. Many thanks Lorna-Jayne Petal & Thread

I would prefer not to have any photgraphs & not too much pink. Thank you!

Industry/Entity Type

Florist

Contact Information for Business Card

Lorna-Jayne Tulk
Floral Designer
0417 635 208
lornajayne@petalandthread.com.au
petalandthread.com.au

Requirements
Must have
• My logo

```html
<!DOCTYPE html>
<html lang="en">
<head>
<meta charset="utf-8">
<title>Petal &amp; Thread — Business Card</title>
<link href="https://fonts.googleapis.com/css2?family=Della+Respira&family=Lato:wght@400;700;900&display=swap" rel="stylesheet">
<style>
  :root {
    --backdrop: #e3e0da;
    --card: #fbf9f4;
    --card-shade: #eeeae1;
    --ink: #1e1c19;
    --ink-mid: #4a4640;
    --ink-soft: #b8b3ab;
    --accent: #c25a8f;
    --shadow: rgba(40, 30, 20, 0.22);
  }
  * { margin: 0; padding: 0; box-sizing: border-box; }
  html, body {
    width: 1200px;
    height: 900px;
    overflow: hidden;
    background: var(--backdrop);
  }
  .canvas {
    position: relative;
    width: 1200px;
    height: 900px;
  }
  .card {
    position: absolute;
    width: 640px;
    height: 366px;
    background: linear-gradient(160deg, var(--card) 40%, var(--card-shade) 100%);
    box-shadow: 0 10px 28px var(--shadow);
  }
  .card--front { left: 80px; top: 70px; }
  .card--back  { left: 480px; top: 464px; }

  .brand {
    display: flex;
    align-items: center;
    gap: 16px;
    font-family: "Della Respira", Georgia, serif;
    font-weight: 400;
    color: var(--ink);
    white-space: nowrap;
  }
  .brand__dot {
    flex: none;
    border-radius: 50%;
    background: var(--accent);
  }
  .card--front .brand {
    position: absolute;
    left: 50%;
    top: 50%;
    transform: translate(-50%, -50%);
    font-size: 66px;
  }
  .card--front .brand__dot { width: 22px; height: 22px; }

  .card--back .brand {
    position: absolute;
    right: 44px;
    top: 40px;
    font-size: 30px;
    gap: 10px;
  }
  .card--back .brand__dot { width: 11px; height: 11px; }

  .holder {
    position: absolute;
    left: 44px;
    top: 118px;
    font-family: "Lato", Arial, sans-serif;
    text-transform: uppercase;
    line-height: 1.15;
  }
  .holder__name {
    font-weight: 900;
    font-size: 21px;
    color: var(--ink-soft);
    letter-spacing: 0.5px;
  }
  .holder__role {
    font-weight: 900;
    font-size: 21px;
    color: var(--ink);
  }
  .contact {
    position: absolute;
    left: 44px;
    top: 190px;
    list-style: none;
    font-family: "Lato", Arial, sans-serif;
    font-weight: 400;
    font-size: 15px;
    line-height: 1.6;
    color: var(--ink-mid);
  }
  .contact__label {
    display: inline-block;
    width: 18px;
    font-weight: 700;
    color: var(--accent);
  }
  .services {
    position: absolute;
    left: 44px;
    bottom: 44px;
    font-family: "Lato", Arial, sans-serif;
    font-weight: 900;
    font-size: 18px;
    color: var(--ink);
    text-transform: uppercase;
  }
</style>
</head>
<body>
<main class="canvas">
  <section class="card card--front" aria-label="Business card front">
    <div class="brand">
      <span class="brand__dot"></span>
      <span class="brand__name">Petal &amp; Thread</span>
    </div>
  </section>

  <section class="card card--back" aria-label="Business card back">
    <div class="brand">
      <span class="brand__dot"></span>
      <span class="brand__name">Petal &amp; Thread</span>
    </div>
    <div class="holder">
      <p class="holder__name">Lorna-Jayne Tulk</p>
      <p class="holder__role">Floral Designer &amp; Owner</p>
    </div>
    <ul class="contact">
      <li><span class="contact__label">P</span>0417 635 208</li>
      <li><span class="contact__label">E</span>lornajayne@petalandthread.com.au</li>
      <li><span class="contact__label">W</span>petalandthread.com.au</li>
    </ul>
    <p class="services">Weddings &amp; Special Occasions</p>
  </section>
</main>
</body>
</html>
```